Solar Advertising Flier to generate Biz

I need a advertisement that generates business to be used in a mailer for marketing purposes.

Im attaching a file that is a an idea of advertisement.
I do not want the "ZVN" specific information on it.
I want the background solar panels.
Same information as the ad.
And I've attached my Logo - I want the color scheme to match this.

Thank you

Target Market(s)

Middle to Upper Class Home Owners

Industry/Entity Type

Solar Energy

Requirements
Must have
• A call to action
• A professional look
Nice to have
• A family
• Great looking solar panels
Should not have
• Cartoons

```html
<!DOCTYPE html>
<html lang="en">
<head>
<meta charset="utf-8">
<title>Go Solar Flier</title>
<link href="https://fonts.googleapis.com/css2?family=Archivo+Black&family=Arimo:wght@400;700&display=swap" rel="stylesheet">
<style>
:root{
  --page:#f2f3f4;
  --sky-top:#5aa6dd;
  --sky-mid:#8cc6ec;
  --roof:#3c3f44;
  --brick:#a4714f;
  --panel:#2d4a7a;
  --blue:#1c7cc4;
  --blue-dark:#0f5c99;
  --green:#7dbb2c;
  --white:#ffffff;
  --ink:#16181b;
  --rule:rgba(28,124,196,.55);
}
*{box-sizing:border-box;margin:0;padding:0}
html,body{width:1200px;height:862px;overflow:hidden;background:var(--page)}
.flier{position:absolute;left:310px;top:21px;width:580px;height:820px;overflow:hidden;font-family:"Arimo",Arial,sans-serif;box-shadow:0 6px 24px rgba(0,0,0,.18)}
.flier__photo{position:absolute;inset:0;
  background:
    linear-gradient(168deg,transparent 0 52%,var(--roof) 52.2% 62%,var(--panel) 62.2% 80%,transparent 80.2%),
    linear-gradient(180deg,transparent 0 72%,var(--brick) 72% 100%),
    linear-gradient(180deg,var(--sky-top) 0%,var(--sky-mid) 45%,#9fd0f0 60%)}
.brand{position:absolute;top:26px;left:0;width:100%;text-align:center}
.brand__mark{display:block;width:58px;height:58px;margin:0 auto 8px;border-radius:50%;background:var(--white);border:4px solid var(--blue)}
.brand__name{font-weight:700;font-size:19px;letter-spacing:1px;color:var(--blue-dark)}
.headline{position:absolute;top:124px;left:0;width:100%;text-align:center;white-space:nowrap;font-family:"Archivo Black",Arial,sans-serif;font-size:86px;line-height:1;color:var(--white);-webkit-text-stroke:9px var(--blue);paint-order:stroke fill;letter-spacing:1px}
.tagline{position:absolute;top:228px;left:0;width:100%;text-align:center;white-space:nowrap;font-weight:700;font-size:19px;color:var(--blue);-webkit-text-stroke:4px var(--white);paint-order:stroke fill;letter-spacing:.3px}
.benefits{position:absolute;top:268px;left:60px;width:460px;list-style:none}
.benefit{display:flex;align-items:center;gap:16px;height:50px;border-top:1px solid var(--rule);font-weight:700;font-size:16px;line-height:1.2;color:var(--ink);-webkit-text-stroke:3px var(--white);paint-order:stroke fill}
.benefit:first-child{border-top:none}
.benefit__icon{flex:0 0 34px;width:34px;height:34px}
.how{position:absolute;top:500px;left:50px;width:470px;background:var(--green);border:4px solid var(--white);border-radius:18px;padding:14px 22px 16px;color:var(--white);font-size:15.5px;line-height:1.4}
.how__tail{position:absolute;right:40px;bottom:-26px;width:0;height:0;border-left:26px solid transparent;border-top:26px solid var(--green)}
.how__title{font-family:"Archivo Black",Arial,sans-serif;font-size:24px;line-height:1.2;color:var(--blue);-webkit-text-stroke:5px var(--white);paint-order:stroke fill;margin-bottom:4px}
.how strong{font-weight:700}
.call{position:absolute;top:718px;left:40px;width:500px;height:88px;background:var(--white);border:5px solid var(--blue);border-radius:44px;display:flex;align-items:center;padding-left:12px;gap:16px}
.call__icon{width:62px;height:62px;flex:0 0 62px}
.call__label{font-family:"Archivo Black",Arial,sans-serif;font-size:28px;line-height:1;color:var(--green);-webkit-text-stroke:5px var(--ink);paint-order:stroke fill}
.call__number{font-family:"Archivo Black",Arial,sans-serif;font-size:38px;line-height:1.05;color:var(--ink)}
</style>
</head>
<body>
<main class="flier">
  <div class="flier__photo" role="img" aria-label="Photo of a tiled house roof fitted with solar panels under a blue sky with white clouds"></div>

  <header class="brand">
    <span class="brand__mark"></span>
    <span class="brand__name">BRIGHT PATH ENERGY</span>
  </header>

  <h1 class="headline">GO SOLAR</h1>
  <p class="tagline">GET GRANDFATHERED BEFORE THE NEW DEADLINE</p>

  <ul class="benefits">
    <li class="benefit">
      <svg class="benefit__icon" viewBox="0 0 34 34"><circle cx="17" cy="17" r="15" fill="#fff" stroke="#1c7cc4" stroke-width="2.5"/><text x="17" y="23" text-anchor="middle" font-family="Arimo,Arial,sans-serif" font-weight="700" font-size="17" fill="#7dbb2c">$</text></svg>
      $0 Down, no upfront cost.
    </li>
    <li class="benefit">
      <svg class="benefit__icon" viewBox="0 0 34 34"><circle cx="17" cy="17" r="15" fill="#1c7cc4"/><path d="M9 22 L17 10 L25 22" fill="none" stroke="#7dbb2c" stroke-width="3"/></svg>
      Save 95% off your utility bill.
    </li>
    <li class="benefit">
      <svg class="benefit__icon" viewBox="0 0 34 34"><path d="M17 3 L29 8 V17 C29 25 23 30 17 32 C11 30 5 25 5 17 V8 Z" fill="#fff" stroke="#1c7cc4" stroke-width="2.5"/><path d="M19 9 L13 19 H18 L15 26" fill="none" stroke="#7dbb2c" stroke-width="2.5"/></svg>
      Protect yourself from rising energy costs
    </li>
    <li class="benefit">
      <svg class="benefit__icon" viewBox="0 0 34 34"><rect x="3" y="9" width="28" height="17" rx="2" fill="#1c7cc4" stroke="#fff" stroke-width="2"/><path d="M3 17.5 H31 M12 9 V26 M22 9 V26" stroke="#fff" stroke-width="1.5"/></svg>
      Provide clean, reliable energy for your family powered by the sun.
    </li>
  </ul>

  <section class="how">
    <h2 class="how__title">How it works...</h2>
    <p>Your solar system allows you to generate your own clean power and <strong>COSTS LESS</strong> than your current utility company. Simply pay by the month, like you do know... but at a <strong>LOWER</strong> rate and <strong>START SAVING IMMEDIATELY</strong>.</p>
    <span class="how__tail"></span>
  </section>

  <section class="call">
    <svg class="call__icon" viewBox="0 0 62 62"><circle cx="31" cy="31" r="29" fill="#1c7cc4"/><circle cx="31" cy="31" r="22" fill="#fff"/><path d="M22 19 C20 21 20 26 25 33 C30 40 36 43 39 42 L42 39 L37 34 L34 36 C31 35 27 31 26 28 L28 25 L23 19 Z" fill="#1c7cc4"/></svg>
    <div>
      <div class="call__label">CALL US TODAY</div>
      <div class="call__number">555 210 486</div>
    </div>
  </section>
</main>
</body>
</html>
```